Business Card for Wellness Clinic

We need a business card for our new logo. I want it to match the feel of the logo

Target Market(s)

Young professional families looking for holistic health care

Industry/Entity Type

Health And Wellness

Contact Information for Business Card

Our business Name: Brackenfield Health & wellness Centre, our phone #, email address...see attached old business card

Font styles to use
Sans Serif

Colors
33b8a4
cee9f5

Requirements
Must have
• my logo and business name
• Font is "Helvetica Neue LT Std 45 Light" and
• Only for "&" using font "Trajan pro bold"
• Use colors in the logo

```html
<!DOCTYPE html>
<html lang="en">
<head>
<meta charset="utf-8">
<title>Brackenfield Health &amp; Wellness Centre – Business Card</title>
<link href="https://fonts.googleapis.com/css2?family=Roboto:wght@300;400&display=swap" rel="stylesheet">
<style>
  :root {
    --teal: #2db5a2;
    --ink-grey: #8a8a8a;
    --rule-grey: #9a9a9a;
    --card: #ffffff;
    --backdrop: #ecefee;
  }
  * { box-sizing: border-box; margin: 0; padding: 0; }
  html, body { width: 1189px; height: 1200px; overflow: hidden; }
  body {
    background: var(--backdrop);
    font-family: "Roboto", "Helvetica Neue", Arial, sans-serif;
    font-weight: 300;
    position: relative;
  }
  .card {
    position: absolute;
    left: 171px;
    width: 856px;
    height: 488px;
    background: var(--card);
    border-radius: 24px;
    overflow: hidden;
    box-shadow: 0 6px 16px rgba(0,0,0,0.18);
  }
  .card--front { top: 67px; }
  .card--back { top: 625px; }

  /* Front */
  .brand-mark {
    position: absolute; left: 396px; top: 62px;
    width: 64px; height: 64px; background: var(--teal); border-radius: 8px;
  }
  .brand-name {
    position: absolute; left: 0; right: 0; top: 176px;
    text-align: center; color: var(--teal);
    font-size: 27px; letter-spacing: 9px; line-height: 40px;
  }
  .doctor {
    position: absolute; right: 458px; top: 316px; text-align: right;
  }
  .doctor__name { color: var(--teal); font-size: 29px; font-weight: 400; line-height: 34px; }
  .doctor__title { color: var(--ink-grey); font-size: 23px; line-height: 32px; }
  .divider {
    position: absolute; left: 428px; top: 310px; width: 2px; height: 90px; background: var(--teal);
  }
  .contacts { position: absolute; left: 454px; top: 310px; list-style: none; }
  .contacts li {
    display: flex; align-items: center; height: 30px; margin-bottom: 0;
    color: var(--ink-grey); font-size: 24px;
  }
  .contacts svg { width: 27px; height: 27px; margin-right: 9px; flex: none; }
  .address-band {
    position: absolute; left: 0; right: 0; bottom: 0; height: 63px;
    background: var(--teal); color: #fff; font-size: 22px;
    display: flex; align-items: center; justify-content: center; font-weight: 400;
  }

  /* Back */
  .rule { position: absolute; height: 2px; background: var(--rule-grey); }
  .rule--name { left: 64px; width: 723px; top: 142px; }
  .appt-heading {
    position: absolute; left: 0; right: 0; top: 162px; text-align: center;
    color: var(--ink-grey); font-size: 33px;
  }
  .days { position: absolute; left: 63px; top: 240px; width: 740px; height: 30px; }
  .day { position: absolute; top: 0; display: flex; align-items: flex-end; }
  .day__box { width: 29px; height: 29px; border: 1.5px solid var(--rule-grey); }
  .day__label { margin-left: 18px; color: var(--ink-grey); font-size: 20px; line-height: 22px; transform: translateY(6px); }
  .field-label { position: absolute; color: var(--ink-grey); font-size: 22px; }
  .rule--date { left: 157px; width: 295px; top: 327px; }
  .rule--time { left: 517px; width: 214px; top: 327px; }
  .meridiem { position: absolute; left: 748px; top: 298px; color: var(--ink-grey); font-size: 21px; line-height: 21px; }
  .policy {
    position: absolute; left: 0; right: 0; top: 398px; text-align: center;
    color: var(--teal); font-size: 22px; line-height: 29px;
  }
</style>
</head>
<body>

<section class="card card--front" aria-label="Business card front">
  <div class="brand-mark" aria-hidden="true"></div>
  <p class="brand-name">BRACKENFIELD HEALTH &amp;<br>WELLNESS CENTRE</p>

  <div class="doctor">
    <p class="doctor__name">DR. MAREN HOLT, N.D.</p>
    <p class="doctor__title">Naturopathic Doctor</p>
  </div>
  <div class="divider"></div>

  <ul class="contacts">
    <li>
      <svg viewBox="0 0 27 27" aria-hidden="true"><rect width="27" height="27" rx="4" fill="#2db5a2"/><path d="M9 6 l3 0 l1 4 l-2 1.5 c1 2.5 2.5 4 4.5 5 l1.5-2 l4 1 l0 3 c-7 1-13-5-12-12.5z" fill="#fff"/></svg>
      613-555-0142
    </li>
    <li>
      <svg viewBox="0 0 27 27" aria-hidden="true"><rect width="27" height="27" rx="4" fill="#2db5a2"/><rect x="5" y="8" width="17" height="12" fill="none" stroke="#fff" stroke-width="1.6"/><path d="M5 8 l8.5 7 l8.5-7" fill="none" stroke="#fff" stroke-width="1.6"/></svg>
      mholt@brackenfieldwellness.ca
    </li>
    <li>
      <svg viewBox="0 0 27 27" aria-hidden="true"><rect width="27" height="27" rx="4" fill="#2db5a2"/><g fill="none" stroke="#fff" stroke-width="1.4"><circle cx="13.5" cy="13.5" r="8"/><ellipse cx="13.5" cy="13.5" rx="3.5" ry="8"/><path d="M5.5 13.5h16M7 9.5h13M7 17.5h13"/></g></svg>
      www.brackenfieldwellness.ca
    </li>
  </ul>

  <div class="address-band">48 Alder Row, Suite 3, Ottawa, ON K1A 0B1</div>
</section>

<section class="card card--back" aria-label="Appointment card back">
  <div class="rule rule--name"></div>
  <p class="appt-heading">Has An Appointment On</p>

  <div class="days">
    <div class="day" style="left:0"><span class="day__box"></span><span class="day__label">Mon</span></div>
    <div class="day" style="left:126px"><span class="day__box"></span><span class="day__label">Tues</span></div>
    <div class="day" style="left:252px"><span class="day__box"></span><span class="day__label">Wed</span></div>
    <div class="day" style="left:379px"><span class="day__box"></span><span class="day__label">Thur</span></div>
    <div class="day" style="left:505px"><span class="day__box"></span><span class="day__label">Fri</span></div>
    <div class="day" style="left:631px"><span class="day__box"></span><span class="day__label">Sat</span></div>
  </div>

  <span class="field-label" style="left:63px; top:305px">Date</span>
  <div class="rule rule--date"></div>
  <span class="field-label" style="left:473px; top:305px">AT</span>
  <div class="rule rule--time"></div>
  <p class="meridiem">am.<br>pm.</p>

  <p class="policy">If you are unable to keep your appointment, please provide at least<br>2 business days notice or full visit fees will apply.</p>
</section>

</body>
</html>
```